bRv Design Group - architect web site

need a web site to permit potential clients to view our portfolio of work.

Will need lots of photos included.

Industry/Entity Type

Architect

Coding

Coded - Design and coding required

Number of Pages Required

5+ page

Font styles to use
Sans Serif

Requirements
Must have
• photos should be organized by project - perhaps a summary of photos and then click to enlarge? should be simple to operate. should be able to separate interior design from architecture.
• needs to be easy to add more photos in the future.

```html
<!DOCTYPE html>
<html lang="en">
<head>
<meta charset="utf-8">
<title>BRV Design Group</title>
<link href="https://fonts.googleapis.com/css2?family=Open+Sans:ital,wght@0,400;0,600;1,400&display=swap" rel="stylesheet">
<style>
:root{
  --teal:#0f8197;
  --teal-dark:#0c6f84;
  --nav:#4c4c4c;
  --nav-dark:#3a3a3a;
  --ink:#2b2b2b;
  --muted:#8a8a8a;
  --rule:#ececec;
  --footer:#2a2a2a;
  --footer-base:#1d1d1d;
  --white:#ffffff;
}
*{margin:0;padding:0;box-sizing:border-box}
html,body{width:703px;height:1200px;overflow:hidden;background:var(--white)}
body{position:relative;font-family:"Open Sans",Arial,sans-serif;color:var(--ink)}
.abs{position:absolute}
.topline{left:0;top:0;width:703px;height:2px;background:var(--teal)}
.topinfo{top:21px;font-size:6.5px;color:var(--muted);display:flex;align-items:center;gap:7px;font-family:Arial,sans-serif}
.hero{left:0;top:53px;width:703px;height:304px;background:linear-gradient(100deg,#5a96ae 0%,#8ec0d3 30%,#c7e1ea 55%,#eef6f9 75%,#d9ebf2 100%)}
.nav{left:58px;top:53px;width:587px;height:38px;background:linear-gradient(#555,var(--nav-dark));box-shadow:0 3px 6px rgba(0,0,0,.25)}
.nav a{position:absolute;top:14px;font-size:7.2px;color:var(--white);text-decoration:none;font-family:Arial,sans-serif}
.nav .dot{position:absolute;top:17px;width:3px;height:3px;border-radius:50%;background:var(--white)}
.brand{left:308px;top:29px;width:86px;height:86px;border-radius:50%;background:#777;border:3px solid #555;display:flex;align-items:center;justify-content:center;text-align:center;color:var(--white);font-size:11px;font-weight:600;line-height:1.2}
.hero-title{left:312px;top:186px;font-size:21px;color:#2f3b44;letter-spacing:.2px}
.hero-sub{left:315px;top:218px;font-size:7.8px;color:#3b4a55;font-family:Arial,sans-serif}
.hero-arrow{top:242px;width:22px;height:22px;background:rgba(255,255,255,.25);display:flex;align-items:center;justify-content:center}
.services{left:0;top:357px;width:703px;height:139px;background:linear-gradient(var(--teal),var(--teal-dark))}
.center{left:0;width:703px;text-align:center}
.services h2{font-weight:400;font-size:18px;color:var(--white)}
.services-intro{top:411px;left:60px;width:583px;text-align:center;font-size:6.6px;line-height:13px;color:var(--white);font-family:Arial,sans-serif}
.service{top:449px;width:150px;text-align:center}
.service .photo{width:94px;height:94px;margin:0 auto;border-radius:50%;border:4px solid var(--white);box-shadow:0 2px 5px rgba(0,0,0,.35)}
.service h3{margin-top:14px;font-size:10px;font-weight:600;letter-spacing:.3px}
.service p{margin-top:5px;font-size:6.3px;line-height:10px;color:var(--muted);font-family:Arial,sans-serif;padding:0 10px}
.more{width:26px;height:26px;border-radius:50%;background:#555;border:2px solid #ccc;box-shadow:0 0 0 1px #555;color:var(--white);font-size:6.5px;font-weight:600;display:flex;align-items:center;justify-content:center;margin:12px auto 0}
.divider{left:58px;width:587px;height:5px;background:var(--rule)}
.section-title{font-weight:400;color:var(--ink)}
.lead{top:723px;font-size:7.6px;font-style:italic;color:#555;font-family:Arial,sans-serif}
.body-text{top:737px;left:62px;width:579px;text-align:center;font-size:6.2px;line-height:14px;color:var(--muted);font-family:Arial,sans-serif}
.btn{left:312px;top:778px;width:57px;height:23px;background:#555;border:2px solid #999;box-shadow:0 0 0 1px #555;color:var(--white);font-size:6.8px;display:flex;align-items:center;justify-content:center;font-family:Arial,sans-serif}
.gallery{left:91px;top:894px;width:521px;height:98px;display:flex}
.gallery div{flex:1;border-right:1px solid #fff}
.footer{left:0;top:1034px;width:703px;height:132px;background:var(--footer)}
.footer-base{left:0;top:1166px;width:703px;height:34px;background:var(--footer-base);color:#bbb;font-size:6.5px;text-align:center;line-height:34px}
.f-head{top:1055px;font-size:8px;font-weight:600;color:var(--white)}
.links{top:1079px;left:62px;list-style:none}
.links li{font-size:5.8px;color:#ccc;line-height:12px;padding-left:9px;position:relative}
.links li::before{content:"";position:absolute;left:0;top:5px;width:3px;height:3px;border-radius:50%;background:#ccc}
.signup{left:178px;top:1082px;width:155px;height:20px;border:1px solid #111;background:#1b1b1b;display:flex;align-items:center;justify-content:space-between;padding:0 2px 0 9px}
.signup span{font-size:5.6px;color:#bbb}
.signup b{background:var(--teal);color:var(--white);font-weight:400;font-size:7.5px;width:44px;height:16px;display:flex;align-items:center;justify-content:center;border-radius:2px}
.contact-row{left:384px;font-size:5.8px;color:#ccc;display:flex;align-items:center;gap:6px}
.contact-row svg{width:11px;height:9px}
.social{top:1082px;width:16px;height:16px}
</style>
</head>
<body>
<div class="abs topline"></div>
<div class="abs topinfo" style="left:97px">
  <svg width="8" height="8" viewBox="0 0 10 10"><path d="M2 0l2 2-1 2c1 1 2 2 3 3l2-1 2 2-2 2C4 10 0 6 0 2z" fill="#555"/></svg>
  <span>CAll Us : 555 210 4400</span>
</div>
<div class="abs topinfo" style="left:506px">
  <svg width="9" height="7" viewBox="0 0 10 8"><rect width="10" height="8" fill="#555"/><path d="M0 0l5 4 5-4" stroke="#fff" fill="none"/></svg>
  <span>info@ brvdesigngroup.com</span>
</div>

<div class="abs hero" role="img" aria-label="Photo of a bright office interior with window blinds and city view"></div>

<nav class="abs nav">
  <a style="left:69px">HOME</a><span class="dot" style="left:107px"></span>
  <a style="left:125px">ABOUT</a><span class="dot" style="left:165px"></span>
  <a style="left:184px">SERVICES</a>
  <a style="left:362px">PORTFOLIO</a><span class="dot" style="left:417px"></span>
  <a style="left:438px">BLOG</a><span class="dot" style="left:473px"></span>
  <a style="left:493px">CONTACTS</a>
</nav>
<div class="abs brand">BRV<br>Design Group</div>

<div class="abs hero-title">BRV DESIGN GROUP</div>
<div class="abs hero-sub">Lorem ipsum dolor sit amet, consectetuer adipiscing elit. Aenean commodo ligula eget dolor.</div>
<div class="abs hero-arrow" style="left:315px"><svg width="6" height="8" viewBox="0 0 6 8"><path d="M5 0L1 4l4 4" stroke="#fff" fill="none"/></svg></div>
<div class="abs hero-arrow" style="left:340px"><svg width="6" height="8" viewBox="0 0 6 8"><path d="M1 0l4 4-4 4" stroke="#fff" fill="none"/></svg></div>

<section class="abs services"></section>
<h2 class="abs center services" style="top:376px;height:auto;background:none">OUR SERVICES</h2>
<p class="abs services-intro">Lorem ipsum dolor sit amet, consectetuer adipiscing elit. Aenean commodo ligula eget dolor. Aenean massa. Cum sociis natoque penatibus et magnis dis parturient montes, nascetur ridiculus mus. Donec quam felis, ultricies nec, pellentesque eu, pretium quis, sem. Nulla consequat massa quis enim. Donec pede justo, fringilla</p>

<div class="abs service" style="left:55px">
  <div class="photo" role="img" aria-label="Dining room with long table and chandelier" style="background:linear-gradient(#d8d2c8,#7d6a58)"></div>
  <h3>LOREM IPSUM</h3>
  <p>Lorem ipsum dolor sit amet, consectetuer adipiscing elit. Aenean commodo ligula eget dolor. Aenean massa. Cum</p>
  <div class="more">More</div>
</div>
<div class="abs service" style="left:200px">
  <div class="photo" role="img" aria-label="White kitchen with island and pendant lights" style="background:linear-gradient(#e6e2dc,#5a4538)"></div>
  <h3>DOLOR SIT</h3>
  <p>Lorem ipsum dolor sit amet, consectetuer adipiscing elit. Aenean commodo ligula eget dolor. Aenean massa. Cum</p>
  <div class="more">More</div>
</div>
<div class="abs service" style="left:352px">
  <div class="photo" role="img" aria-label="Minimal white bathroom" style="background:linear-gradient(#eef0f0,#8e9494)"></div>
  <h3>CONSECTETUER</h3>
  <p>Lorem ipsum dolor sit amet, consectetuer adipiscing elit. Aenean commodo ligula eget dolor. Aenean massa. Cum</p>
  <div class="more">More</div>
</div>
<div class="abs service" style="left:497px">
  <div class="photo" role="img" aria-label="Curved staircase under tall windows" style="background:linear-gradient(#cfe2ee,#f2f2f2 60%,#6a6a6a)"></div>
  <h3>ADIPISCING ELIT</h3>
  <p>Lorem ipsum dolor sit amet, consectetuer adipiscing elit. Aenean commodo ligula eget dolor. Aenean massa. Cum</p>
  <div class="more">More</div>
</div>

<div class="abs divider" style="top:657px"></div>
<h2 class="abs center section-title" style="top:681px;font-size:19px">WELCOME TO BRV DESIGN GROUP</h2>
<p class="abs center lead">Lorem ipsum dolor sit amet, consectetuer adipiscing elit. Aenean commodo ligula eget dolor. Aenean massa.</p>
<p class="abs body-text">Cum sociis natoque penatibus et magnis dis parturient montes, nascetur ridiculus mus. Donec quam felis, ultricies nec, pellentesque eu, pretium quis, sem. Nulla consequat massa quis enim. Donec pede justo, fringilla vel, aliquet nec, vulputate eget, arcu. In enim justo, rhoncus ut, imperdiet a, venenatis vitae, justo. Nullam dictum felis eu pede mollis pretium.quis enim.</p>
<div class="abs btn">READ MORE</div>

<div class="abs divider" style="top:820px"></div>
<h2 class="abs center section-title" style="top:845px;font-size:17px">LATEST PORTFOLIO</h2>
<svg class="abs" style="left:58px;top:932px" width="12" height="20" viewBox="0 0 12 20"><path d="M10 1L2 10l8 9" stroke="#d4d4d4" stroke-width="2" fill="none"/></svg>
<svg class="abs" style="left:633px;top:932px" width="12" height="20" viewBox="0 0 12 20"><path d="M2 1l8 9-8 9" stroke="#d4d4d4" stroke-width="2" fill="none"/></svg>
<div class="abs gallery">
  <div role="img" aria-label="Bright living room opening onto a garden" style="background:linear-gradient(#e4e0da,#b8ad9e)"></div>
  <div role="img" aria-label="White villa with palm trees and pool" style="background:linear-gradient(#2a5f8a,#3d5a3a 70%,#1f2f22)"></div>
  <div role="img" aria-label="Open-plan living space with timber beams" style="background:linear-gradient(#e8e2da,#6a4a34)"></div>
  <div role="img" aria-label="Outdoor terrace with stone fireplace" style="background:linear-gradient(#4a4440,#a8a49e)"></div>
</div>

<footer class="abs footer"></footer>
<div class="abs f-head" style="left:62px">QUICK LINKS</div>
<ul class="abs links">
  <li>Home</li><li>About Us</li><li>Services</li><li>Portfolio</li><li>Testimonials</li><li>Contact Us</li>
</ul>
<div class="abs f-head" style="left:178px">NEWS LETTER SIGNUP</div>
<div class="abs signup"><span>Enter your email here</span><b>Send</b></div>
<div class="abs f-head" style="left:384px">CONTACT</div>
<div class="abs contact-row" style="top:1080px"><svg viewBox="0 0 11 9"><path d="M1 3c3-3 6-3 9 0v2H8V4H3v1H1z M2 6h7v3H2z" fill="#aaa"/></svg>Phone: (555) 210 4400 789</div>
<div class="abs contact-row" style="top:1094px"><svg viewBox="0 0 11 9"><rect x="1" y="1" width="9" height="7" fill="#aaa"/><path d="M1 1l4.5 4 4.5-4" stroke="#2a2a2a" fill="none"/></svg>Email: info@brvdesigngroup.com</div>
<div class="abs contact-row" style="top:1108px"><svg viewBox="0 0 11 9"><path d="M5.5 9L2.5 4.5a3 3 0 1 1 6 0z" fill="#aaa"/><circle cx="5.5" cy="3.5" r="1.2" fill="#2a2a2a"/></svg>Address: Street Name ,City</div>
<div class="abs contact-row" style="top:1123px;left:401px">Street Name ,City</div>
<div class="abs f-head" style="left:552px">FOLLOW US ON</div>
<div class="abs social" style="left:552px;background:#3b5a98"></div>
<div class="abs social" style="left:576px;background:#2a9fd8"></div>
<div class="abs social" style="left:599px;background:#d42626"></div>
<div class="abs social" style="left:622px;background:#f28a1c"></div>
<div class="abs footer-base">Copyright 2015 &nbsp;BRV Design Group | &nbsp;All Rights Reserved.</div>
</body>
</html>
```